Law Office needs stationery design and business card

I currently have been using the same letterhead for the last 8 years. Since i 'm about to adding another location, I want to revamp my letterhead and business card. I already have a logo i'm happy with. I will upload my current letterhead, fax sheet, envelope, and logos. I need a business card also. I have 2 locations, 1 phone number, 1 fax line, website, etc. If possible and fitting with the design, I would like to keep the same information listed currently on the letterhead.

**Keep in mind, I also NEED A FAX SHEET COVER. thank you
Updates

Hello, Please submit a Gray Scale or Black and White version of your designs also, since most of the time I will be printing NON color stationery. I will seldom use a color print for my letterhead, I would like to have a color version for my benefit, however i will print in grayscale majority of the time . For the Business Card, that can just be in color. When I get my business cards they will be in color.Thank youEnrique Added Sunday, September 18, 2016

Industry/Entity Type

Business

```html
<!DOCTYPE html>
<html lang="en">
<head>
<meta charset="utf-8">
<title>Marlowe Law – Envelope</title>
<link rel="stylesheet" href="https://fonts.googleapis.com/css2?family=Open+Sans:ital,wght@0,400;0,600;1,700&display=swap">
<style>
  :root {
    --paper: #fdfaf2;
    --paper-light: #fffefb;
    --gold: #bf9c58;
    --gold-soft: #f5deb0;
    --gold-line: #f3e3bd;
    --ink: #1d1a18;
    --tile-light: #fbf3e3;
    --tile-mid: #ebdfc8;
    --tile-edge: #f5eee0;
    --mark-faint: #e9e3d8;
  }
  * { margin: 0; padding: 0; box-sizing: border-box; }
  html, body { width: 1200px; height: 582px; overflow: hidden; background: #ffffff; }
  .envelope {
    position: relative;
    width: 1200px;
    height: 582px;
    overflow: hidden;
    background: var(--paper);
    font-family: "Open Sans", sans-serif;
  }
  .backdrop { position: absolute; inset: 0; }
  .brand {
    position: absolute;
    left: 26px;
    top: 76px;
    width: 300px;
    text-align: center;
  }
  .brand-mark {
    display: inline-flex;
    align-items: center;
    gap: 10px;
    margin-top: 66px;
  }
  .brand-square {
    width: 14px;
    height: 14px;
    background: var(--gold);
  }
  .brand-name {
    font-size: 21px;
    font-weight: 600;
    letter-spacing: 1px;
    color: var(--gold);
  }
  .brand-rule {
    height: 2px;
    margin-top: 6px;
    background: linear-gradient(90deg, var(--gold-line), var(--gold-soft) 50%, rgba(245,222,176,0));
  }
  .attorney {
    margin-top: 6px;
    font-size: 15px;
    font-weight: 700;
    font-style: italic;
    color: var(--gold);
  }
  .contacts {
    position: absolute;
    left: 58px;
    top: 306px;
    list-style: none;
    color: var(--ink);
    font-size: 16px;
    line-height: 29.5px;
  }
  .contacts li { display: flex; align-items: flex-start; }
  .contact-icon { width: 14px; height: 14px; margin: 8px 7px 0 0; flex: none; }
  .contact-text { display: block; }
</style>
</head>
<body>
<main class="envelope">
  <svg class="backdrop" width="1200" height="582" viewBox="0 0 1200 582" aria-hidden="true">
    <polygon points="240,0 1200,0 1200,308" fill="var(--paper-light)"/>
    <polygon points="0,270 0,582 900,582" fill="#fbf7ec" opacity="0.5"/>
    <rect class="faint-square" x="318" y="345" width="200" height="200" fill="var(--mark-faint)" opacity="0.7"/>
    <rect x="1000" y="314" width="138" height="139" rx="5" fill="var(--tile-light)"/>
    <rect x="898" y="394" width="88" height="88" rx="4" fill="var(--tile-mid)"/>
    <rect x="897" y="494" width="89" height="92" rx="4" fill="var(--tile-light)"/>
    <rect x="1000" y="496" width="110" height="90" rx="4" fill="var(--tile-mid)"/>
    <rect x="1150" y="433" width="54" height="87" rx="4" fill="var(--tile-edge)"/>
    <polygon points="0,566 296,566 290,582 0,582" fill="var(--gold-soft)"/>
    <polygon points="314,566 1200,566 1200,582 308,582" fill="var(--gold)"/>
  </svg>

  <header class="brand">
    <div class="brand-mark">
      <span class="brand-square"></span>
      <span class="brand-name">MARLOWE LAW</span>
    </div>
    <div class="brand-rule"></div>
    <p class="attorney">Tobias Marlowe Esq.</p>
  </header>

  <ul class="contacts">
    <li>
      <svg class="contact-icon" viewBox="0 0 14 14"><circle cx="7" cy="7" r="6.3" fill="none" stroke="var(--gold)" stroke-width="1"/><path d="M7 3.2a2.4 2.4 0 0 1 2.4 2.4c0 1.8-2.4 4.4-2.4 4.4S4.6 7.4 4.6 5.6A2.4 2.4 0 0 1 7 3.2z" fill="var(--gold)"/><circle cx="7" cy="5.6" r="0.9" fill="#fff"/></svg>
      <span class="contact-text">418 Alder St, Brookfield,<br>PA 19320</span>
    </li>
    <li>
      <svg class="contact-icon" viewBox="0 0 14 14"><circle cx="7" cy="7" r="6.3" fill="none" stroke="var(--gold)" stroke-width="1"/><path d="M7 3.2a2.4 2.4 0 0 1 2.4 2.4c0 1.8-2.4 4.4-2.4 4.4S4.6 7.4 4.6 5.6A2.4 2.4 0 0 1 7 3.2z" fill="var(--gold)"/><circle cx="7" cy="5.6" r="0.9" fill="#fff"/></svg>
      <span class="contact-text">145 East Mill St., Suite 200,<br>Oakdale, PA 19075</span>
    </li>
    <li>
      <svg class="contact-icon" viewBox="0 0 14 14"><circle cx="7" cy="7" r="6.3" fill="none" stroke="var(--gold)" stroke-width="1"/><path d="M5 3.6c.5 0 1.2 1.4 1.2 1.8s-.8.6-.6 1.2c.3.9 1 1.6 1.8 1.9.6.2.8-.6 1.2-.6s1.8.7 1.8 1.2c0 .6-.9 1.4-1.6 1.3C6.5 10.1 3.9 7.5 3.6 5.2 3.5 4.5 4.4 3.6 5 3.6z" fill="var(--gold)"/></svg>
      <span class="contact-text">610.555.0142</span>
    </li>
    <li>
      <svg class="contact-icon" viewBox="0 0 14 14"><circle cx="7" cy="7" r="6.3" fill="var(--gold)" opacity="0.25"/><circle cx="7" cy="7" r="6.3" fill="none" stroke="var(--gold)" stroke-width="1"/><rect x="4.8" y="3.6" width="4.4" height="2.2" fill="var(--gold)"/><rect x="3.6" y="6.1" width="6.8" height="3" rx="0.6" fill="var(--gold)"/><rect x="4.8" y="8.4" width="4.4" height="2.2" fill="#fff" stroke="var(--gold)" stroke-width="0.6"/></svg>
      <span class="contact-text">484.555.0187</span>
    </li>
    <li>
      <svg class="contact-icon" viewBox="0 0 14 14"><circle cx="7" cy="7" r="6.3" fill="none" stroke="var(--gold)" stroke-width="1"/><circle cx="7" cy="7" r="3.8" fill="none" stroke="var(--gold)" stroke-width="0.9"/><ellipse cx="7" cy="7" rx="1.6" ry="3.8" fill="none" stroke="var(--gold)" stroke-width="0.8"/><line x1="3.2" y1="7" x2="10.8" y2="7" stroke="var(--gold)" stroke-width="0.8"/></svg>
      <span class="contact-text">www.MarloweLaw.com</span>
    </li>
    <li>
      <svg class="contact-icon" viewBox="0 0 14 14"><circle cx="7" cy="7" r="6.3" fill="none" stroke="var(--gold)" stroke-width="1"/></svg>
      <span class="contact-text">MarloweLaw</span>
    </li>
  </ul>
</main>
</body>
</html>
```